Business Card Design

residential construction discipline, renovation additions, new homes, also sheds, retaining walls and general building maintenance. In house design and construct, estimate or bill of quantities, complete project administration, contract administration. design and construction Negotiations and consultation.complete council submissions for consent. Sustainable design and construction. The design will need to be smart colorful fine line(s), impressive. Font will need to be palatino linotype, the "a" in forlinq will need to be a eco green color and the rest of the lettering black or sky blue. present initial proof design for review
Industry/Entity Type
Construction
Contact Information for Business Card
Forlinq Pty Ltd
ABN: 39 402 817 264
ACN: 402 817 264
Lic/Reg Number: 613047
Director: Trevor Asklund BConstructMgmt&Eco, AssocDegBuiltEnv
Building Works Supervisor
Lic/Reg Number: BLD684210
Email: forlinq@mailbrook.net
Mobile: 0431 958 204
Fax: (08) 8392 5148

```html
<!DOCTYPE html>
<html lang="en">
<head>
<meta charset="utf-8">
<title>Forlinq Pty Ltd – Business Card</title>
<link rel="stylesheet" href="https://fonts.googleapis.com/css2?family=EB+Garamond:wght@500&family=Montserrat:wght@400;500;600&display=swap">
<style>
  :root {
    --bg: #c9cacc;
    --card: #f6f6f4;
    --blue: #2b4a9a;
    --green: #16a35a;
    --ink: #2a2d33;
    --muted: #6a6d73;
    --silver: #d9dadc;
  }
  html, body {
    margin: 0;
    width: 1200px;
    height: 907px;
    overflow: hidden;
    background: var(--bg);
  }
  .canvas { position: relative; width: 1200px; height: 907px; }
  .card {
    position: absolute;
    width: 560px;
    height: 320px;
    background: var(--card);
    overflow: hidden;
    box-shadow: 0 10px 24px rgba(0,0,0,0.18);
  }
  .card--front { left: 90px; top: 90px; }
  .card--back { left: 550px; top: 497px; }
  .card__bands { position: absolute; inset: 0; width: 100%; height: 100%; }
  .brand {
    position: absolute;
    display: flex;
    align-items: center;
    gap: 10px;
    font-family: "EB Garamond", "Palatino Linotype", serif;
    font-weight: 500;
    font-variant: small-caps;
    letter-spacing: 2px;
    color: var(--blue);
  }
  .brand__dot {
    width: 22px; height: 22px;
    border-radius: 50%;
    background: var(--blue);
  }
  .card--front .brand { left: 50%; top: 128px; transform: translateX(-50%); font-size: 30px; }
  .card--front .web {
    position: absolute; right: 104px; bottom: 34px;
    font-family: "Montserrat", sans-serif; font-size: 12px; color: var(--ink);
  }
  .card--back .brand { left: 110px; top: 34px; font-size: 24px; }
  .details {
    position: absolute; left: 120px; top: 92px;
    font-family: "Montserrat", sans-serif; color: var(--ink);
  }
  .details__name { margin: 0; font-size: 14px; font-weight: 600; letter-spacing: 1px; text-transform: uppercase; }
  .details__role { margin: 2px 0 12px; font-size: 12px; font-weight: 500; color: var(--green); }
  .details__address { margin: 0 0 12px; font-size: 11px; line-height: 1.45; color: var(--muted); }
  .contact-list { list-style: none; margin: 0; padding: 0; font-size: 11px; color: var(--muted); }
  .contact-list li { display: flex; align-items: center; gap: 7px; height: 17px; }
  .contact-list svg { width: 11px; height: 11px; fill: var(--green); }
  .card--back .web {
    position: absolute; right: 104px; bottom: 24px;
    font-family: "Montserrat", sans-serif; font-size: 11px; color: var(--ink);
  }
</style>
</head>
<body>
<main class="canvas">

  <section class="card card--front" aria-label="Card front">
    <svg class="card__bands" viewBox="0 0 560 320" preserveAspectRatio="none" aria-hidden="true">
      <path d="M0 0 L70 0 C40 100 40 220 90 320 L0 320 Z" fill="var(--blue)"/>
      <path d="M80 0 C50 100 50 220 102 320" fill="none" stroke="var(--green)" stroke-width="4"/>
      <path d="M92 0 C62 100 62 220 116 320" fill="none" stroke="var(--silver)" stroke-width="2"/>
      <path d="M560 0 L560 320 L480 320 C520 220 520 100 490 0 Z" fill="var(--blue)"/>
      <path d="M478 0 C508 100 508 220 468 320" fill="none" stroke="var(--green)" stroke-width="4"/>
      <path d="M466 0 C496 100 496 220 454 320" fill="none" stroke="var(--silver)" stroke-width="2"/>
    </svg>
    <div class="brand"><span class="brand__dot"></span>Forlinq Pty Ltd</div>
    <p class="web">www.forlinqbuild.net</p>
  </section>

  <section class="card card--back" aria-label="Card back">
    <svg class="card__bands" viewBox="0 0 560 320" preserveAspectRatio="none" aria-hidden="true">
      <path d="M0 0 L60 0 C34 100 34 220 80 320 L0 320 Z" fill="var(--blue)"/>
      <path d="M70 0 C44 100 44 220 92 320" fill="none" stroke="var(--silver)" stroke-width="3"/>
      <path d="M560 0 L560 320 L490 320 C528 220 528 100 500 0 Z" fill="var(--blue)"/>
      <path d="M488 0 C516 100 516 220 478 320" fill="none" stroke="var(--silver)" stroke-width="3"/>
    </svg>
    <div class="brand"><span class="brand__dot"></span>Forlinq Pty Ltd</div>
    <div class="details">
      <p class="details__name">Ellis Harwood</p>
      <p class="details__role">Managing Director</p>
      <p class="details__address">27 Kestrel Lane<br>Norwood SA</p>
      <ul class="contact-list">
        <li><svg viewBox="0 0 12 12"><path d="M2 1h3l1 3-1.5 1a6 6 0 0 0 2.5 2.5L8 6l3 1v3a1 1 0 0 1-1 1A9 9 0 0 1 1 2a1 1 0 0 1 1-1z"/></svg>08 8391 2740</li>
        <li><svg viewBox="0 0 12 12"><path d="M2 1h3l1 3-1.5 1a6 6 0 0 0 2.5 2.5L8 6l3 1v3a1 1 0 0 1-1 1A9 9 0 0 1 1 2a1 1 0 0 1 1-1z"/></svg>08 8391 2741</li>
        <li><svg viewBox="0 0 12 12"><path d="M2 1h3l1 3-1.5 1a6 6 0 0 0 2.5 2.5L8 6l3 1v3a1 1 0 0 1-1 1A9 9 0 0 1 1 2a1 1 0 0 1 1-1z"/></svg>08 8391 2742</li>
        <li><svg viewBox="0 0 12 12"><path d="M1 2.5h10v7H1z M1 2.5l5 4 5-4" /></svg>office@forlinqbuild.net</li>
      </ul>
    </div>
    <p class="web">www.forlinqbuild.net</p>
  </section>

</main>
</body>
</html>
```